Q7 Engineering Rail Sector Brochure

We need a new 3 page folding brochure for Q7 Engineering Pty Ltd. The organisation is currently supporting customers in Defence, Maritime and Information and Communications Technology companies. We are currently looking to expand our engineering services into the rail sector by providing manpower and consultancy services to railway sector clients.We would like the brochure to be based on an A4 page and look technical with particular focus on communications systems used within the railways. This could include pictures of rail control centres, trains (Australian trains only please), train radio communications equipment, radio antennas, computers and networking equipment. Please use both graphics and photos.The brochure will be provided to potential rail customers and should be clear and uncluttered.The following is our company website: www.q7engineering.com.au if you would like more detail on our current work.I have attached the file for our logo which should appear on the brochure.
Target Market(s)
Providing manpower and consultancy services to the railway sector. This includes rail companies (e.g. Harwick Loop Trains, T/Run etc) and rail equipment and carriage suppliers (e.g. Falverine)
Colors
Designer to choose colors to be used in the design.
Requirements
Must have
- Instead of having "lorem ipsum" text in the brochure you can please use some of the text in the file we have provided. Not all has to be used, and you should not be limited to what is in the file.
Nice to have
- Mixture of different font sizes to highlight particular text elements.

```html
<!DOCTYPE html>
<html lang="en">
<head>
<meta charset="utf-8">
<title>Q7 Engineering – Rail Sector Brochure</title>
<link href="https://fonts.googleapis.com/css2?family=Open+Sans:wght@400;600;700&family=Montserrat:wght@800&display=swap" rel="stylesheet">
<style>
  :root {
    --blue: #1f44a8;
    --blue-deep: #16318a;
    --ink: #1b1f2a;
    --white: #ffffff;
    --paper: #eef0f3;
    --stage: #4a4a4c;
    --bar: #1d1d1f;
  }
  * { box-sizing: border-box; margin: 0; padding: 0; }
  html, body { width: 1200px; height: 800px; overflow: hidden; background: var(--stage); }
  body { font-family: "Open Sans", sans-serif; color: var(--white); }
  .brochure { position: absolute; left: 30px; top: 20px; width: 1140px; height: 760px; background: var(--paper); overflow: hidden; }
  .brochure-art { position: absolute; inset: 0; }
  .fold { position: absolute; top: 0; bottom: 0; width: 1px; background: rgba(0,0,0,.08); }
  .fold--one { left: 380px; } .fold--two { left: 760px; }
  .panel { position: absolute; top: 0; width: 380px; height: 760px; }
  .panel--inside { left: 0; } .panel--back { left: 380px; } .panel--cover { left: 760px; }

  .intro { position: absolute; left: 36px; top: 58px; width: 310px; font-weight: 700; font-size: 16.5px; line-height: 1.35; }
  .rule { width: 34px; height: 4px; border-radius: 2px; background: var(--white); margin: 16px 0 14px; }
  .rule--center { margin: 10px auto; background: var(--blue); width: 24px; height: 3px; }
  .service-list { list-style: none; font-size: 12.5px; font-weight: 400; line-height: 1.4; }
  .service-list li { position: relative; padding-left: 18px; margin-bottom: 7px; }
  .service-list li::before { content: "✓"; position: absolute; left: 0; top: 0; font-weight: 700; }
  .staff-statement { position: absolute; left: 36px; top: 528px; width: 320px; color: var(--ink); font-weight: 600; font-size: 17.5px; line-height: 1.32; }

  .capabilities { position: absolute; left: 40px; top: 140px; width: 300px; font-size: 11px; line-height: 1.5; text-align: center; }
  .capabilities p + p { margin-top: 12px; }
  .contact-box { position: absolute; left: 70px; top: 430px; width: 240px; border: 1.5px solid rgba(255,255,255,.55); border-radius: 12px; padding: 12px 10px; text-align: center; font-size: 12px; line-height: 1.45; }
  .contact-box strong { font-weight: 700; display: block; }
  .contact-box .gap { display: block; margin-top: 8px; }
  .office { position: absolute; left: 0; right: 0; top: 612px; text-align: center; color: var(--ink); font-size: 12.5px; line-height: 1.7; }
  .office h3 { font-size: 15px; font-weight: 700; }
  .office .line { display: flex; align-items: center; justify-content: center; gap: 6px; }
  .office svg { width: 12px; height: 12px; fill: var(--blue); }

  .brand { position: absolute; top: 70px; left: 0; right: 0; display: flex; align-items: center; justify-content: center; gap: 10px; color: var(--blue-deep); font-size: 30px; font-weight: 600; }
  .brand-dot { width: 18px; height: 18px; border-radius: 50%; background: var(--blue-deep); }
  .headline { position: absolute; left: 48px; top: 280px; font-family: "Montserrat", sans-serif; font-weight: 800; font-size: 27px; line-height: 1.2; text-transform: uppercase; }
  .cover-rule { position: absolute; left: 48px; top: 432px; width: 30px; height: 4px; border-radius: 2px; background: var(--white); }
  .tagline { position: absolute; left: 48px; top: 452px; width: 300px; font-weight: 600; font-size: 18px; line-height: 1.35; }
  .subline { position: absolute; left: 48px; top: 520px; width: 290px; font-size: 12.5px; text-align: right; line-height: 1.4; }
  .url-bar { position: absolute; left: 48px; top: 568px; width: 290px; background: var(--bar); padding: 5px 12px; font-size: 11.5px; text-align: right; }
  .url-bar b { font-weight: 700; }
</style>
</head>
<body>
<main class="brochure">
  <svg class="brochure-art" viewBox="0 0 1140 760" width="1140" height="760">
    <defs>
      <linearGradient id="photo-tone" x1="0" y1="0" x2="0" y2="1">
        <stop offset="0" stop-color="#dfe7ef"/>
        <stop offset=".55" stop-color="#9fb0c4"/>
        <stop offset="1" stop-color="#e4e6ea"/>
      </linearGradient>
      <linearGradient id="band-tone" x1="0" y1="0" x2="1" y2="1">
        <stop offset="0" stop-color="#1a3ea6"/>
        <stop offset="1" stop-color="#2550b8"/>
      </linearGradient>
    </defs>
    <rect width="1140" height="760" fill="url(#photo-tone)" role="img" aria-label="Photo of an Australian passenger train at a platform under a bright sky"/>
    <path d="M0,0 H380 C470,60 620,90 760,90 C900,90 1000,200 1140,215 V610 C1000,620 900,565 760,565 C620,565 520,515 380,505 C250,495 120,480 0,500 Z" fill="url(#band-tone)" opacity=".93"/>
  </svg>
  <div class="fold fold--one"></div>
  <div class="fold fold--two"></div>

  <section class="panel panel--inside">
    <div class="intro">
      Q7 Engineering provides engineering resources, speciality services and project delivery from concept to completion in areas including:
      <div class="rule"></div>
      <ul class="service-list">
        <li>Command and Control (C2) system integration</li>
        <li>Plain and Secure voice &amp; data TCP/IP communications</li>
        <li>Acoustics, Noise, Shock and Vibration design, analysis and test</li>
        <li>RF System Visualisation, Modelling and Analytics</li>
        <li>Networked systems including VoIP, IPTV, CCTV and Videowall technologies</li>
        <li>Logistics, Training and ongoing program support solutions</li>
      </ul>
    </div>
    <p class="staff-statement">Q7 Engineering staff have been in the forefront of major program deliveries to defence and commercial customers for decades. Our staff are leaders in their field and pioneers in the establishment of systematic approaches to the most complex problems.</p>
  </section>

  <section class="panel panel--back">
    <div class="capabilities">
      <p>At Q7 Engineering we have a broad mix of capabilities, including abilities in the areas of networking, communications, C2 system integration with sensor and communications systems. Our staff have supported the largest telecommunication networks in Australia and aided defence in building real-time, secure data networks for communications and data sharing. We have enabled communications across multiple platforms types including aircraft, rail, ship and vehicle platforms that operate reliably under extreme environmental conditions.</p>
      <p>At Q7 Engineering, we are commited to delivering value to all our customers and end users in a manner that inspires.</p>
    </div>
    <div class="contact-box">
      Career Opportunities:
      <strong>jobs@Q7Engineering.com.au</strong>
      <span class="gap">General Enquiries:</span>
      <strong>info@Q7Engineering.com.au</strong>
    </div>
    <div class="office">
      <h3>Main Office Address:</h3>
      <div class="rule rule--center"></div>
      <p class="line"><svg viewBox="0 0 12 12"><path d="M6 0a4 4 0 0 0-4 4c0 3 4 8 4 8s4-5 4-8a4 4 0 0 0-4-4zm0 5.5A1.5 1.5 0 1 1 6 2.5a1.5 1.5 0 0 1 0 3z"/></svg>Level 4, 18 Larkin St, Calder 3100</p>
      <p class="line"><svg viewBox="0 0 12 12"><circle cx="6" cy="6" r="6"/></svg>www.q7engineering.com.au</p>
    </div>
  </section>

  <section class="panel panel--cover">
    <div class="brand"><span class="brand-dot"></span>Q7 Engineering</div>
    <h1 class="headline">Smart<br>solutions that<br>deliver<br>excellence.</h1>
    <div class="cover-rule"></div>
    <p class="tagline">We deliver solutions to critical challenges.</p>
    <p class="subline">A trusted provider to the world's most exacting customers.</p>
    <p class="url-bar">www.<b>q7engineering</b>.com.au</p>
  </section>
</main>
</body>
</html>
```